Strength and Conditioning Business needs a logo design

We need a logo design for a fitness company based in South Carolina called "K9R Athletic Performance". We are a group of Strength and Conditioning Coaches that work with youth, high school, collegiate, and professional athletes. We also train general population clients that are looking to improve their overall fitness. Our primary mission is to make sure our athletes are able to gain the greatest benefits from training that will allow them to excel in their sport. We use heavy chains, kettle bells, resistance bands, dumbbells, prowlers (sleds), and multi-functional machines for training. We have a dynamic and collaborative approach that utilizes high-intensity intervals combined with speed, power, agility, and strength training.

Industry/Entity Type

Fitness

Contact Information for Business Card

K9R Athletic Performance
Lorenzo Pike, MEd, CSCS, PES
Head of Athletic Development
Greenville, SC
Phone: (864) 517-3084
Email: k9rathleticperformance@mailbox-example.com
Instagram: iron_trainer_v

Font styles to use
Sans Serif

Colors
9bcb3c
ffffff
000000
474747
ec1f27
7f7f7f
0456a4

Requirements
Must have
• I would like to have a black card with either lime green or bold blue accents along with white and silver. On the back, I would like the name 'K9R Athletic Performance' with a subheading that says, 'Strength and Conditioning.'
Nice to have
• I really like the designs of the cards I uploaded. For the logo, something clean, bold, and eye-catching would be great.
Should not have
• I do not want a logo that will make it difficult to read.

```html
<!DOCTYPE html>
<html lang="en">
<head>
<meta charset="utf-8">
<title>K9R Athletic Performance – Business Card</title>
<link href="https://fonts.googleapis.com/css2?family=Montserrat:wght@600&family=Oswald:wght@300;400;500&display=swap" rel="stylesheet">
<style>
  :root {
    --card-black: #1f1e1e;
    --lime: #9bcb3c;
    --white: #ffffff;
    --silver: #d9d9d9;
    --page: #e6e6e4;
  }
  * { box-sizing: border-box; margin: 0; padding: 0; }
  html, body { width: 1200px; height: 900px; overflow: hidden; }
  body { background: var(--page); position: relative; font-family: "Oswald", sans-serif; }

  .card {
    position: absolute;
    left: 250px;
    width: 700px;
    height: 400px;
    background: var(--card-black);
    color: var(--white);
  }
  .card--back { top: 30px; }
  .card--front { top: 470px; }

  .brand { position: absolute; left: 0; right: 0; text-align: center; }
  .brand__mark {
    font-family: "Montserrat", sans-serif;
    font-weight: 600;
    color: var(--white);
    line-height: 1;
  }
  .brand__mark .brand__code { display: block; }
  .brand__tagline {
    display: flex; align-items: center; justify-content: center; gap: 8px;
    font-family: "Montserrat", sans-serif; font-weight: 600;
    color: var(--lime); text-transform: uppercase; letter-spacing: 0.04em;
  }
  .brand__tagline::before, .brand__tagline::after {
    content: ""; height: 1px; background: var(--lime);
  }

  .card--back .brand { top: 70px; }
  .card--back .brand__code { font-size: 130px; letter-spacing: 0.02em; }
  .card--back .brand__name { display: block; font-size: 30px; letter-spacing: 0.06em; margin-top: 10px; }
  .card--back .brand__tagline { font-size: 16px; margin-top: 12px; }
  .card--back .brand__tagline::before, .card--back .brand__tagline::after { width: 60px; }

  .card--front .brand { top: 34px; }
  .card--front .brand__code { font-size: 70px; letter-spacing: 0.02em; }
  .card--front .brand__name { display: block; font-size: 17px; letter-spacing: 0.06em; margin-top: 5px; }
  .card--front .brand__tagline { font-size: 9.5px; margin-top: 6px; }
  .card--front .brand__tagline::before, .card--front .brand__tagline::after { width: 34px; }

  .profile {
    position: absolute; left: 20px; top: 228px; width: 260px;
    text-align: right; line-height: 1.3;
  }
  .profile__name { color: var(--lime); font-size: 31px; font-weight: 500; text-transform: uppercase; line-height: 1.2; }
  .profile__line { font-size: 21px; font-weight: 300; }

  .divider {
    position: absolute; left: 292px; top: 218px; width: 2px; height: 160px;
    background: var(--lime);
  }

  .contacts {
    position: absolute; left: 310px; top: 252px; list-style: none;
  }
  .contact { display: flex; align-items: center; gap: 8px; height: 42px; font-size: 22px; font-weight: 300; }
  .contact__icon {
    width: 28px; height: 28px; border-radius: 50%; background: var(--lime);
    flex: none; display: flex; align-items: center; justify-content: center;
  }
  .contact__icon svg { width: 16px; height: 16px; }
  .contact--email { font-size: 17px; }
</style>
</head>
<body>

<section class="card card--back" aria-label="Card back">
  <div class="brand">
    <p class="brand__mark"><span class="brand__code">K9R</span><span class="brand__name">ATHLETIC PERFORMANCE</span></p>
    <p class="brand__tagline">Strength and Conditioning</p>
  </div>
</section>

<section class="card card--front" aria-label="Card front">
  <div class="brand">
    <p class="brand__mark"><span class="brand__code">K9R</span><span class="brand__name">ATHLETIC PERFORMANCE</span></p>
    <p class="brand__tagline">Strength and Conditioning</p>
  </div>

  <div class="profile">
    <p class="profile__name">Lorenzo Pike</p>
    <p class="profile__line">MEd, CSCS, PES</p>
    <p class="profile__line">Head of Athletic Development</p>
    <p class="profile__line">Greenville, SC</p>
  </div>

  <div class="divider"></div>

  <ul class="contacts">
    <li class="contact">
      <span class="contact__icon">
        <svg viewBox="0 0 24 24"><path fill="#1f1e1e" d="M6.6 10.8a15.1 15.1 0 0 0 6.6 6.6l2.2-2.2c.3-.3.7-.4 1-.2 1.1.4 2.3.6 3.6.6.6 0 1 .4 1 1V20c0 .6-.4 1-1 1A17 17 0 0 1 3 4c0-.6.4-1 1-1h3.5c.6 0 1 .4 1 1 0 1.3.2 2.5.6 3.6.1.3 0 .7-.2 1z"/></svg>
      </span>
      <span>(864) 517-3084</span>
    </li>
    <li class="contact contact--email">
      <span class="contact__icon">
        <svg viewBox="0 0 24 24"><rect x="3" y="6" width="18" height="12" rx="1" fill="#1f1e1e"/><path d="M3.5 6.5 12 13l8.5-6.5" fill="none" stroke="#9bcb3c" stroke-width="1.6"/></svg>
      </span>
      <span>k9rathleticperformance@mailbox-example.com</span>
    </li>
    <li class="contact">
      <span class="contact__icon"></span>
      <span>iron_trainer_v</span>
    </li>
  </ul>
</section>

</body>
</html>
```